Corvella Website Homepage

Committed to delivering quality content, quillpagewords.com is a content providing company. Equipped with resourceful writers with industry experience, we promise to empower our clients with content that is tailor-made to address specific requirements of their target Audience.

We need a website home page and one internal page designed. It is very important that the page be laid out with SEO in mind. We like the idea of using five images as navigation to our services. The five major services we offer are:
• Web Content writing (articles, features, website copy etc)
• Business Content writing (Press release, mailers & flyers, brochure/catalog)
• Personal Content writing (blog, speech writing)
• Hire a writer/editor
• Proof reading and editing services
The sample template (http://pv7.layoutdemo-hub.net/dx_48270/index.html) included has five images in the first fold. Designer can choose the right image for each service and lay over the service name on the image. Please do not use flash ( We will use javascripts). We need to have a detailed right side nav as in the template for SEO reasons. There will be some marketing ad- copy below the main images. Followed by a 200 character SEO optimized text defining our services in further detail. Apart from these a designer is free to use his creativity. The name of the site will be http://www.quillpagewords.com/. This name will need a logo too. Please include it as part of design. Corvellacorp is the owner of quillpagewords.com. We already have a logo for Corvella that is attached here as a separate file.

We have some taglines that need to be incorporated in the home page and other pages.
Please provide link button for Home, About us, Services, Samples, Pricing, Clients, Career, Contact us.

Links can be given on TOP, Sideways and Bottom and in the drop down menu of services etc.

Reason: Hi

We have made our project guaranteed and extended deadline by 5 days so you get more time to complete our project.

Thanks and Regards,

Ravindra Kulkarni
Corvellacorp

Target Market(s)

Product Marketing Companies - Mostly in US.
Media companies which publish articles on various subjects. Travel and Lifestyle related sites, Educational Websites, Government Websites, Health related websites,

Industry/Entity Type

Marketing

Requirements
Must have
• Color of Homepage should blend with sober mood of the content. Writing Services should get highlighted in such a way that any person serious about the business visiting the site get attracted to read on the details of our content services. Most space should be used for details of writing services and links for our various pages and services. Webpage should be downloaded in lowest possible time.
Nice to have
• We have some idea about the website layouts;-http://www.skinbazaarly.net/site-layouts/48270.html - layout of information http://www.skinbazaarly.net/site-layouts/47359.html - for kind of marketing http://pv7.layoutdemo-hub.net/dx_48615/index.html - for colors
we attach a word file representing our idea in some way but not limited to it.
Should not have
• Gaudy (aggressive dark) colors. It should not be cluttered. No flash.

```html
<!DOCTYPE html>
<html lang="en">
<head>
<meta charset="utf-8">
<title>QuillPageWords.com – Content Writing Services</title>
<link rel="stylesheet" href="https://fonts.googleapis.com/css2?family=Open+Sans:ital,wght@0,400;0,600;1,400&family=Arimo:wght@400;700&display=swap">
<style>
:root{
  --brand:#2e9fe0;
  --brand-dark:#1d86c9;
  --nav-top:#45b3ea;
  --nav-bottom:#1e8cd0;
  --nav-active:#5cc3f2;
  --link:#2b8fd6;
  --heading-blue:#3aa3e6;
  --heading-grey:#5b6168;
  --muted-blue:#9fc3dc;
  --text:#5f6469;
  --text-dark:#3a4a57;
  --rule:#d6e6f2;
  --footer-bg:#eef6fb;
  --page:#ffffff;
  --flank:#e7e8ea;
}
*{margin:0;padding:0;box-sizing:border-box}
html,body{width:971px;height:1200px;overflow:hidden;background:var(--page)}
body{position:relative;font-family:"Arimo",Arial,sans-serif;color:var(--text)}
a{color:inherit;text-decoration:none}
.top-strip{position:absolute;left:0;top:0;width:971px;height:8px;background:var(--brand)}
.site-header{position:absolute;left:0;top:8px;width:971px;height:83px;background:linear-gradient(180deg,#fff 0%,#f5fafd 100%)}
.logo{position:absolute;left:84px;top:30px;display:flex;align-items:center;gap:9px;font-family:"Open Sans",sans-serif;font-weight:600;font-size:25px;color:var(--brand);letter-spacing:-.2px}
.logo-dot{width:20px;height:20px;border-radius:50%;background:var(--brand)}
.main-nav{position:absolute;left:0;top:91px;width:971px;height:47px;background:linear-gradient(180deg,var(--nav-top),var(--nav-bottom))}
.main-nav ul{list-style:none;display:flex;position:absolute;left:76px;top:0;height:47px}
.main-nav li{display:flex;align-items:center;height:47px;padding:0 10px;font-family:"Open Sans",sans-serif;font-size:12.5px;color:#fff;position:relative}
.main-nav li+li::before{content:"";position:absolute;left:0;top:16px;height:16px;border-left:1px solid rgba(255,255,255,.55)}
.main-nav li.is-active{background:var(--nav-active)}
.main-nav li.is-active::before,.main-nav li.is-active+li::before{display:none}
.hero-flank{position:absolute;top:138px;height:322px;width:46px;background:linear-gradient(180deg,var(--flank),#f4f5f6)}
.service-tiles{position:absolute;left:46px;top:138px;width:877px;height:322px;display:flex}
.service-tile{position:relative;flex:1;height:322px}
.tile-photo{position:absolute;inset:0 0 62px 0}
.tile-caption{position:absolute;left:0;right:0;bottom:0;height:62px;padding:10px 0 0 16px;color:#fff;font-family:"Open Sans",sans-serif}
.tile-caption strong{display:block;font-weight:600;font-size:20.5px;line-height:26px}
.tile-caption span{display:block;font-size:12px;font-weight:600;color:#d8ecfa;line-height:16px}
.service-tile:nth-child(odd) .tile-caption{background:#3ea2e6}
.service-tile:nth-child(even) .tile-caption{background:#3394d8}
.promise{position:absolute;left:87px;top:476px;width:480px;font-family:"Open Sans",sans-serif;font-style:italic;font-size:17px;line-height:26px;color:#7d8a94}
.promise-rule{position:absolute;left:46px;top:566px;width:580px;height:1px;background:linear-gradient(90deg,transparent,var(--rule) 20%,var(--rule) 80%,transparent)}
.about-photo{position:absolute;left:65px;top:591px;width:157px;height:215px;background:linear-gradient(180deg,#e9eef2,#c9d3dc)}
.about{position:absolute;left:233px;top:586px;width:358px}
.about h2{font-size:14px;font-weight:700;color:var(--text-dark);margin-bottom:5px;font-family:"Open Sans",sans-serif;font-weight:600}
.about p{font-size:10.6px;line-height:15.6px;color:var(--text)}
.read-more{position:absolute;right:0;top:200px;font-size:11px;font-weight:700;color:var(--link)}
.sidebar{position:absolute;left:635px;top:460px;width:336px;height:356px;background:linear-gradient(90deg,#f3f8fc,#fff 40%)}
.sidebar h3{position:absolute;left:41px;top:22px;font-size:19px;font-weight:700;color:var(--heading-grey)}
.offer-list{position:absolute;left:41px;top:60px;width:228px;list-style:none}
.offer-list li{height:23.1px;border-bottom:1px solid var(--rule);font-size:12.6px;color:var(--link);padding:4px 0 0 13px;position:relative}
.offer-list li:last-child{border-bottom:none}
.offer-list li::before{content:"";position:absolute;left:0;top:8px;border-left:5px solid #4a5560;border-top:3px solid transparent;border-bottom:3px solid transparent}
.section-rule{position:absolute;left:46px;top:823px;width:877px;height:1px;background:linear-gradient(90deg,transparent,var(--rule) 15%,var(--rule) 85%,transparent)}
.why{position:absolute;left:85px;top:838px;font-size:19px;font-weight:700;color:var(--heading-blue)}
.why em{font-style:normal;color:var(--muted-blue)}
.feature{position:absolute;display:flex;align-items:center;gap:0;font-size:14px;line-height:19px;color:var(--text-dark)}
.feature svg{flex:none}
.feature span{position:absolute}
.clients-title{position:absolute;left:675px;top:838px;font-size:19px;font-weight:700;color:var(--heading-blue)}
.client-grid{position:absolute;left:646px;top:880px;display:grid;grid-template-columns:repeat(3,84px);grid-auto-rows:42px;column-gap:9px;row-gap:13px}
.client-slot{border:2px solid #e2eef7;background:#fff}
.client-slot svg{display:block}
.more-clients{position:absolute;right:57px;top:1046px;font-size:11px;font-weight:700;color:var(--link)}
.site-footer{position:absolute;left:0;top:1076px;width:971px;height:124px;background:linear-gradient(180deg,#e9f4fb,var(--footer-bg))}
.footer-links{position:absolute;left:83px;top:21px;font-size:11.2px;color:var(--text-dark)}
.footer-links a.is-current{text-decoration:underline}
.copyright{position:absolute;left:83px;top:78px;font-size:11.2px;color:#6b7075}
.newsletter-title{position:absolute;left:638px;top:19px;font-size:13.5px;font-weight:700;color:var(--text-dark);display:flex;align-items:center;gap:8px}
.newsletter-input{position:absolute;left:638px;top:48px;width:187px;height:20px;border:2px solid #cfe0ec;background:#fff;font-size:10px;font-style:italic;color:#b4bcc3;padding:3px 0 0 14px}
.subscribe{position:absolute;left:840px;top:48px;width:73px;height:20px;background:linear-gradient(180deg,#2fb0f0,#0b87d6);border:1px solid #0a78c0;color:#fff;font-size:11.5px;font-weight:700;text-align:center;line-height:18px}
.social{position:absolute;left:638px;top:86px;display:flex;align-items:center;font-size:11.5px;font-weight:700;color:#3b6d93}
.social i{display:inline-block;width:12px;height:12px;background:#3d6fb3;margin:0 16px 0 10px}
.social i.alt{background:#6cc6ec}
</style>
</head>
<body>
<div class="top-strip"></div>
<header class="site-header">
  <a class="logo" href="http://www.quillpagewords.com/">QuillPageWords.com<span class="logo-dot"></span></a>
</header>
<nav class="main-nav">
  <ul>
    <li>HOME</li><li>ABOUT US</li><li class="is-active">SERVICES</li><li>SAMPLES</li><li>PRICING</li><li>CLIENTS</li><li>CAREER</li><li>CONTACT US</li>
  </ul>
</nav>

<div class="hero-flank" style="left:0"></div>
<div class="hero-flank" style="left:923px"></div>
<section class="service-tiles">
  <a class="service-tile"><div class="tile-photo" role="img" aria-label="Office computer monitors and keyboards in blue tint" style="background:linear-gradient(160deg,#dfe9f2,#8fb0c8 60%,#3b6485)"></div><div class="tile-caption"><strong>Web</strong><span>content writing</span></div></a>
  <a class="service-tile"><div class="tile-photo" role="img" aria-label="Hand writing with a pen in blue tint" style="background:linear-gradient(160deg,#8fb3d1,#5f8db4 55%,#8aaecb)"></div><div class="tile-caption"><strong>Business</strong><span>content writing</span></div></a>
  <a class="service-tile"><div class="tile-photo" role="img" aria-label="Pen resting on a handwritten page" style="background:linear-gradient(160deg,#eef3f8,#c7d7e5 55%,#dfe8f0)"></div><div class="tile-caption"><strong>Personal</strong><span>content writing</span></div></a>
  <a class="service-tile"><div class="tile-photo" role="img" aria-label="Portrait of a thoughtful writer in blue tint" style="background:linear-gradient(160deg,#3e6c93,#6f96b8 50%,#1f4466)"></div><div class="tile-caption"><strong>Hire</strong><span>writer or editor</span></div></a>
  <a class="service-tile"><div class="tile-photo" role="img" aria-label="Close-up of printed text being proofread" style="background:linear-gradient(160deg,#c3d6e6,#e8f0f6 55%,#a9c3d9)"></div><div class="tile-caption"><strong>Proofreading</strong><span>editing services</span></div></a>
</section>

<aside class="sidebar">
  <h3>What we offer</h3>
  <ul class="offer-list">
    <li>Urgent Translation</li><li>Legal Translation</li><li>Patent Translation</li><li>Medical Translation</li><li>Technical Translation</li><li>Marketing Translation</li><li>Financial Translation</li><li>Persosal Translation</li><li>Website Translation</li><li>Proofreading</li><li>Transcription</li><li>Voiceovers</li>
  </ul>
</aside>

<p class="promise">We promise to empower our clients with content that is tailor-made to address specific requirements of their target Audience.</p>
<div class="promise-rule"></div>

<div class="about-photo" role="img" aria-label="Smiling businesswoman writing on a clipboard"></div>
<article class="about">
  <h2>About Quillpagewords</h2>
  <p>Lorem ipsum dolor sit amet, consectetur adipiscing elit. Donec sagittis, lorem nec interdum convallis, lacus tellus vulputate libero, a dapibus sapien nulla vel arcu. Cras eu nibh neque. Nulla facilisi. Vestibulum mauris dolor, porta sed hendrerit in, pretium ut velit. Donec nisl magna, cursus non accumsan vel, tempus ut nibh. In erat orci, sagittis ut sodales ut, varius id sem.</p>
  <p>Nullam posuere scelerisque turpis eu interdum. Mauris vel mauris non purus venenatis dignissim. Fusce et neque vel turpis condimentum vehicula. Aliquam eget purus eu eros pulvinar aliquam. Donec mattis, est id rhoncus ultricies, leo sapien blandit mi, quis faucibus leo ligula a dolor. Maecenas.</p>
  <a class="read-more" href="#">read more</a>
</article>

<div class="section-rule"></div>

<h2 class="why">Why choose <em>Quillpagewords</em>:</h2>

<div class="feature" style="left:65px;top:884px"><svg width="30" height="30" viewBox="0 0 30 30"><circle cx="15" cy="15" r="14" fill="#dfe6f0" stroke="#9aa7b8"/><rect x="4" y="13" width="22" height="4" fill="#c8202f"/><rect x="13" y="3" width="4" height="24" fill="#c8202f"/></svg><span style="left:52px;top:5px;white-space:nowrap">English - American and British</span></div>
<div class="feature" style="left:65px;top:928px"><svg width="32" height="32" viewBox="0 0 32 32"><circle cx="12" cy="12" r="9" fill="#e8f3fb" stroke="#5b87b0" stroke-width="3"/><path d="M19 19l9 9" stroke="#c98a2a" stroke-width="4" stroke-linecap="round"/></svg><span style="left:52px;top:-2px;width:200px">Optimized content for search engines</span></div>
<div class="feature" style="left:65px;top:974px"><svg width="30" height="32" viewBox="0 0 30 32"><rect x="4" y="1" width="20" height="27" fill="#f4f8fb" stroke="#9fb3c4"/><circle cx="14" cy="19" r="7" fill="#fff" stroke="#5b87b0" stroke-width="2"/><path d="M9 24l-6 6" stroke="#6b8a3a" stroke-width="3"/></svg><span style="left:52px;top:7px;white-space:nowrap">Intensive Research</span></div>
<div class="feature" style="left:68px;top:1016px"><svg width="28" height="34" viewBox="0 0 28 34"><path d="M7 18l-3 15 6-4 4 5 2-14z M21 18l3 15-6-4-4 5-2-14z" fill="#e2812a"/><circle cx="14" cy="12" r="10" fill="#f2c23a" stroke="#d39a1c" stroke-width="2"/></svg><span style="left:49px;top:-2px;width:180px">Team of subject Matter Experts</span></div>

<div class="feature" style="left:330px;top:884px"><svg width="28" height="30" viewBox="0 0 28 30"><rect x="1" y="15" width="7" height="14" fill="#3f8fd8"/><rect x="10" y="8" width="7" height="21" fill="#8cc63e"/><rect x="19" y="2" width="7" height="27" fill="#e8473a"/></svg><span style="left:50px;top:6px;white-space:nowrap">Success stories of our clients</span></div>
<div class="feature" style="left:328px;top:928px"><svg width="32" height="30" viewBox="0 0 32 30"><path d="M3 5l10 14" stroke="#5a5f66" stroke-width="3"/><rect x="11" y="10" width="14" height="11" transform="rotate(28 18 15)" fill="#c99455"/><circle cx="14" cy="24" r="3" fill="#555"/></svg><span style="left:53px;top:6px;white-space:nowrap">Ultra high speed delivery</span></div>
<div class="feature" style="left:328px;top:974px"><svg width="32" height="30" viewBox="0 0 32 30"><ellipse cx="16" cy="17" rx="13" ry="10" fill="#f08a2c"/><rect x="8" y="24" width="4" height="5" fill="#d56f18"/><rect x="20" y="24" width="4" height="5" fill="#d56f18"/><rect x="13" y="5" width="6" height="3" fill="#b35a10"/></svg><span style="left:49px;top:-5px;width:160px">Competitive Cost on our services</span></div>

<h2 class="clients-title">Our Clients</h2>
<div class="client-grid">
  <div class="client-slot"><svg width="80" height="38"><path d="M0 0L80 38M80 0L0 38" stroke="#e2eef7"/></svg></div>
  <div class="client-slot"><svg width="80" height="38"><path d="M0 0L80 38M80 0L0 38" stroke="#e2eef7"/></svg></div>
  <div class="client-slot"><svg width="80" height="38"><path d="M0 0L80 38M80 0L0 38" stroke="#e2eef7"/></svg></div>
  <div class="client-slot"><svg width="80" height="38"><path d="M0 0L80 38M80 0L0 38" stroke="#e2eef7"/></svg></div>
  <div class="client-slot"><svg width="80" height="38"><path d="M0 0L80 38M80 0L0 38" stroke="#e2eef7"/></svg></div>
  <div class="client-slot"><svg width="80" height="38"><path d="M0 0L80 38M80 0L0 38" stroke="#e2eef7"/></svg></div>
  <div class="client-slot"><svg width="80" height="38"><path d="M0 0L80 38M80 0L0 38" stroke="#e2eef7"/></svg></div>
  <div class="client-slot"><svg width="80" height="38"><path d="M0 0L80 38M80 0L0 38" stroke="#e2eef7"/></svg></div>
  <div class="client-slot"><svg width="80" height="38"><path d="M0 0L80 38M80 0L0 38" stroke="#e2eef7"/></svg></div>
</div>
<a class="more-clients" href="#">more about our clients</a>

<footer class="site-footer">
  <nav class="footer-links"><a>Home</a> | <a>About us</a> | <a class="is-current">Services</a> | <a>Samples</a> | <a>Pricing</a> | <a>Clients</a> | <a>Career</a> | <a>Contact us</a></nav>
  <p class="copyright">Copyright 2011 © QuillPageWords.com</p>
  <div class="newsletter-title">Newsletter <svg width="15" height="11" viewBox="0 0 15 11"><rect x="1" y="1" width="13" height="9" fill="none" stroke="#2b8fd6" stroke-width="1.6"/><path d="M1 1l6.5 5L14 1" fill="none" stroke="#2b8fd6" stroke-width="1.6"/></svg></div>
  <div class="newsletter-input">your e-mail</div>
  <div class="subscribe">Subscribe</div>
  <div class="social">Become a fan<i></i>Follow us<i class="alt"></i></div>
</footer>
</body>
</html>
```